Web design for a Crane & Heavy Equipment Inspection, Repair and Maintenance Company in Texas

We need a web design for a new company based in Houston, Texas called "Bristen Hoist & Equipment". We inspect, repair and maintain diesel driven heavy equipment, generators, fire water pumps and cranes. We would like to see designs that use the colors orange, white, yellow and brown, and/or orange, white, navy, yellow and grey.

```html
<!DOCTYPE html>
<html lang="en">
<head>
<meta charset="utf-8">
<title>Bristen Hoist &amp; Equipment</title>
<link rel="stylesheet" href="https://fonts.googleapis.com/css2?family=Open+Sans:wght@400;600;700;800&family=Questrial&display=swap">
<style>
:root{
  --orange:#f05a28;
  --orange-light:#f57a45;
  --orange-dark:#d4461a;
  --navy:#1d4a7c;
  --text:#666;
  --heading:#55453e;
  --band:#f2f2f2;
  --info:#e9eaea;
  --footer:#2c2c2c;
  --white:#fff;
}
*{margin:0;padding:0;box-sizing:border-box}
html,body{width:688px;height:1200px;overflow:hidden;background:var(--white)}
body{position:relative;font-family:"Open Sans",Arial,sans-serif;color:var(--text)}
.abs{position:absolute}

.brand{left:49px;top:40px;color:var(--orange);font-weight:800;line-height:1}
.brand-name{font-size:31px;letter-spacing:-0.5px}
.brand-sub{font-size:16px;margin-top:4px;padding-left:88px;letter-spacing:.5px}
.phone{right:18px;top:53px;color:var(--navy);font-size:15px;display:flex;align-items:center;gap:7px}
.search{left:488px;top:88px;width:150px;height:20px;border:1px solid #ccc;font-size:9px;color:#888;padding:4px 7px;display:flex;justify-content:space-between;align-items:center}

.nav{left:0;top:132px;width:688px;height:34px;background:linear-gradient(var(--orange-light),var(--orange));border-top:1px solid var(--orange-dark)}
.nav a{position:absolute;top:0;height:33px;line-height:33px;text-align:center;color:var(--white);font-size:10px;font-weight:700;text-decoration:none;border-right:1px solid rgba(255,255,255,.25)}
.nav a.active{background:var(--orange-dark)}

.hero{left:0;top:166px;width:688px;height:283px;background:linear-gradient(180deg,#7c7a74 0%,#9a958a 45%,#8b7d66 100%)}
.hero-crane{left:100px;top:0;width:430px;height:283px;background:linear-gradient(135deg,#f2b418,#d88d0c)}
.hero-caption{left:162px;top:127px;width:262px;background:rgba(40,40,40,.6);padding:11px 14px 12px;color:var(--white)}
.hero-caption h2{font-family:"Questrial",sans-serif;font-size:18px;font-weight:400;line-height:22px;white-space:nowrap;margin-bottom:4px}
.hero-caption p{font-size:9px;line-height:14.5px}
.hero-arrow{top:117px;width:22px;height:36px;background:rgba(60,60,60,.6);display:flex;align-items:center;justify-content:center}

.welcome{left:52px;top:480px;width:584px;text-align:center}
.welcome h1{font-family:"Questrial",sans-serif;font-weight:400;font-size:21px;color:var(--heading)}
.welcome h1 .o{color:var(--orange)}
.welcome h1 .n{color:var(--navy)}
.welcome p{font-size:7.8px;line-height:14.5px;margin-top:12px}
.btn{display:inline-block;margin-top:13px;background:var(--navy);color:var(--white);font-size:10.5px;padding:5px 12px;border-radius:2px}

.services{left:0;top:621px;width:688px;height:241px;background:var(--band)}
.service{top:36px;width:177px;text-align:center}
.service .photo{width:177px;height:99px}
.service h3{font-size:11.5px;font-weight:600;color:var(--navy);margin-top:17px}
.service p{font-size:8.2px;line-height:14.5px;margin-top:7px}

.testimonials h2{position:absolute;left:0;top:893px;width:688px;text-align:center;font-family:"Questrial",sans-serif;font-weight:400;font-size:20px;color:var(--heading)}
.avatar-ring{left:55px;top:911px;width:110px;height:110px;border-radius:50%;background:#f4f4f4;box-shadow:0 1px 4px rgba(0,0,0,.15)}
.avatar{left:60px;top:916px;width:100px;height:100px;border-radius:50%;background:radial-gradient(circle at 50% 40%,#d9d9d9,#bdbdbd)}
.quote-badge{left:133px;top:990px;width:38px;height:38px;border-radius:50%;background:#eee;border:3px solid var(--white);color:#aaa;font-size:28px;font-weight:800;text-align:center;line-height:44px}
.quote{left:200px;top:940px;width:446px;font-size:7.8px;line-height:14.5px}
.quote .mark{position:absolute;color:#aaa;font-size:22px;font-weight:800;line-height:1}
.quote p{padding-left:14px}
.quote .end{color:#aaa;font-size:18px;font-weight:800;line-height:0;vertical-align:-6px}
.quote .who{margin-top:8px;padding-left:14px;color:#333;font-size:9px}
.quote .who b{font-size:10px}

.info{left:0;top:1065px;width:688px;height:66px;background:var(--info)}
.info-item{top:0;height:66px;display:flex;align-items:center;gap:12px;font-family:Arial,sans-serif;color:#555;font-size:9.5px}
.info-sep{top:20px;width:1px;height:27px;background:#ccc}

.footer{left:0;top:1131px;width:688px;height:69px;background:var(--footer);color:#ddd;font-family:Arial,sans-serif;font-size:8px}
.footer .links{position:absolute;left:50px;top:21px}
.footer .copy{position:absolute;left:50px;top:42px}
.social{position:absolute;top:16px;width:21px;height:21px}
</style>
</head>
<body>

<header>
  <div class="abs brand"><div class="brand-name">BRISTEN HOIST</div><div class="brand-sub">&amp; EQUIPMENT</div></div>
  <div class="abs phone">+1 713 555 0148
    <svg width="12" height="13" viewBox="0 0 24 24"><path fill="#1d4a7c" d="M6.6 10.8c1.4 2.8 3.8 5.1 6.6 6.6l2.2-2.2c.3-.3.7-.4 1-.2 1.1.4 2.3.6 3.6.6.6 0 1 .4 1 1V20c0 .6-.4 1-1 1C10.6 21 3 13.4 3 4c0-.6.4-1 1-1h3.5c.6 0 1 .4 1 1 0 1.3.2 2.5.6 3.6.1.3 0 .7-.2 1L6.6 10.8z"/></svg>
  </div>
  <div class="abs search"><span>Search..</span>
    <svg width="9" height="9" viewBox="0 0 10 10"><circle cx="4" cy="4" r="3" fill="none" stroke="#999" stroke-width="1.3"/><path d="M6.3 6.3L9 9" stroke="#999" stroke-width="1.3"/></svg>
  </div>
</header>

<nav class="abs nav">
  <a class="active" style="left:50px;width:70px">HOME</a>
  <a style="left:120px;width:61px">ABOUT</a>
  <a style="left:181px;width:80px">CRANES</a>
  <a style="left:261px;width:127px">SERVICES OFFERED</a>
  <a style="left:388px;width:63px">BLOG</a>
  <a style="left:451px;width:107px">TESTIMONIALS</a>
  <a style="left:558px;width:80px;border-right:none">CONTACT</a>
</nav>

<section class="abs hero" role="img" aria-label="Large yellow mobile crane parked in front of a rock quarry wall with stacked pallets">
  <div class="abs hero-crane"></div>
  <div class="abs hero-caption">
    <h2>AENEAN COMDO AMETI</h2>
    <p>Eodem modo typi, qui nunc nobis videntur parum clari, fiant sollemnes in futurum fiant. Mes cuml dia sed in lacus.</p>
  </div>
  <div class="abs hero-arrow" style="left:0"><svg width="8" height="14"><path d="M7 1L1 7l6 6" fill="none" stroke="#ccc" stroke-width="1.5"/></svg></div>
  <div class="abs hero-arrow" style="right:0"><svg width="8" height="14"><path d="M1 1l6 6-6 6" fill="none" stroke="#ccc" stroke-width="1.5"/></svg></div>
</section>

<section class="abs welcome">
  <h1>Welcome to <span class="o">BRISTEN</span> <span class="n">HOIST &amp; EQUIPMENT</span></h1>
  <p>Typi non habent claritatem insitam; est usus legentis in iis qui facit eorum claritatem. Investigationes demonstraverunt lectores legere me lquod ii unt saepius. Clarit as est etiam processus dynamicus, qui sequitur mutationem consuetudium lectorum. Mirum est notare quam litteothica, quam nunc putamus aramnimut litterarum formas humanitatis per seacula quarta decima et quinta decima. Eodem modo typi, qui nunc nobis videntur parum clari, fiant sollemnes in futurum.</p>
  <span class="btn">Read More</span>
</section>

<section class="abs services">
  <div class="abs service" style="left:48px">
    <div class="photo" role="img" aria-label="Tower cranes silhouetted against a dusk sky" style="background:linear-gradient(180deg,#2f4a6a,#8a8e9a 70%,#2a2a30)"></div>
    <h3>INSPECT</h3>
    <p>Nullam sed nisi arcu condinm varius. Etiam malesuada velit bibeumdonec sit amet orci augue tristique eros amet risus</p>
  </div>
  <div class="abs service" style="left:253px">
    <div class="photo" role="img" aria-label="Welder repairing a red crane boom lattice" style="background:linear-gradient(135deg,#b9c7d6,#c9303a 55%,#8e2028)"></div>
    <h3>REPAIR</h3>
    <p>Nullam sed nisi arcu condinm varius. Etiam malesuada velit bibeumdonec sit amet orci augue tristique eros amet risus</p>
  </div>
  <div class="abs service" style="left:461px">
    <div class="photo" role="img" aria-label="Workers maintaining a crane arm in a workshop" style="background:linear-gradient(180deg,#9a9a9a,#4e4e4e 60%,#6b4b3a)"></div>
    <h3>MAINTAIN</h3>
    <p>Nullam sed nisi arcu condinm varius. Etiam malesuada velit bibeumdonec sit amet orci augue tristique eros amet risus</p>
  </div>
</section>

<section class="testimonials">
  <h2>Testimonials</h2>
  <div class="abs avatar-ring"></div>
  <div class="abs avatar" role="img" aria-label="Portrait photo of the client giving the testimonial"></div>
  <div class="abs quote-badge">&ldquo;</div>
  <div class="abs quote">
    <span class="mark" style="left:0;top:-4px">&ldquo;</span>
    <p>Duis rutrum eros orci, at tristique nulla dictum id. Donec porta justo non justo ultrices mattis. Nullam nec tortor eleifend, molestie quam ac, pretium quam. Nulla at pulvinar purus. Sed tristique elementum sapien sit amet porttitor. Duis eget consectetur et tortor ac libero gravida porttitor at et justo. libero gravida porttitor at et justo. <span class="end">&rdquo;</span></p>
    <div class="who"><b>- Dorian,</b> Norway</div>
  </div>
</section>

<section class="abs info">
  <div class="abs info-item" style="left:66px">
    <svg width="16" height="22" viewBox="0 0 16 22"><path fill="#555" d="M8 0C3.6 0 0 3.4 0 7.7 0 13.5 8 22 8 22s8-8.5 8-14.3C16 3.4 12.4 0 8 0zm0 11a3.2 3.2 0 110-6.4A3.2 3.2 0 018 11z"/></svg>
    <div><div style="font-size:10px">Duis autem vel eum iriureHendrerit.</div><div style="font-size:8.5px;margin-top:4px">Typi non habent claritatem insitam</div></div>
  </div>
  <div class="abs info-sep" style="left:273px"></div>
  <div class="abs info-item" style="left:306px">
    <svg width="17" height="17" viewBox="0 0 24 24"><path fill="#555" d="M6.6 10.8c1.4 2.8 3.8 5.1 6.6 6.6l2.2-2.2c.3-.3.7-.4 1-.2 1.1.4 2.3.6 3.6.6.6 0 1 .4 1 1V20c0 .6-.4 1-1 1C10.6 21 3 13.4 3 4c0-.6.4-1 1-1h3.5c.6 0 1 .4 1 1 0 1.3.2 2.5.6 3.6.1.3 0 .7-.2 1L6.6 10.8z"/></svg>
    <span>713 - 555 - 0190</span>
  </div>
  <div class="abs info-sep" style="left:427px"></div>
  <div class="abs info-item" style="left:462px">
    <svg width="26" height="17" viewBox="0 0 26 17"><rect x="0" y="0" width="26" height="17" fill="#555"/><path d="M1 1l12 9 12-9" fill="none" stroke="#e9eaea" stroke-width="1.5"/></svg>
    <span>info@bristenhoist.com</span>
  </div>
</section>

<footer class="abs footer">
  <div class="links">Terms and Conditions | Privacy Promise | FAQ's | Contact Us</div>
  <div class="copy">Copyright © 2013. All Rights Reserved.</div>
  <span class="social" style="left:507px;background:#3b5998"></span>
  <span class="social" style="left:535px;background:#2ba0d9"></span>
  <span class="social" style="left:563px;background:#f07f1c"></span>
  <span class="social" style="left:591px;background:#d8262b"></span>
</footer>

</body>
</html>
```